Buch-/eBook-Cover für Fitnessübungen für Väter unter Einbezug ihres Babys
Zielgruppe
Kurzbeschreibung: Das Buch enthält Fitnessübungen, die Väter unter Einbezug ihres Babys (zb. als Trainingsgewicht) machen können. Ziel ist es, dass beide Spaß haben, die Papas fitter werden und Zeit mit ihren Kindern verbringen.
Zielgruppe: Das Buch wird als lustiges und unterhaltsames, aber zugleich sinnvolles Geschenk für werdende oder frischgebackene Väter gekauft.
Aufgabenstellung
- Das Cover soll locker, modern-lässig, cool, und spaßig wirken (siehe Samples). Man soll das als Geschenk mit dem dem Gefühl kaufen „ach, das kann einfach nur gut ankommen “
- Nur grafische / illustrierte Konzepte, keine fotobasierten Cover
- Im Anhang drei Illustrationen aus dem Buch. Diese Illustration können Sie für das Cover verwenden und auch bearbeiten. Wir würden uns aber auch freuen, wenn Sie ein eigenes Motiv entwickeln / finden, das besser zu ihrem Cover-Konzept passt und Abwechslung in die Auswahl bringt.
- Bitte laden Sie keine Mockups von hoch. Nur mit einer 'normalen' Datei haben wir einen unverfälschten Eindruck, wie es aussieht
- Seitenverhältnis des Covers: 4:5
- Titel: Kinderwagen-Kraftkurs für starke Väter und fröhliche Kleine („Kinderwagen-Kraftkurs“ sollte am größten sein)
- Untertitel: Mit den 33 besten Fitness-Übungen mit Baby Muskeln stärken, Spaß haben und die Vater-Kind-Bindung vertiefen
- Weiteres Schriftelement: 0-3 Jahre (wie handschriftlich „nachträglich“ dazugeschrieben, am besten mit gezeichnetem Pfeil auf das Baby)
- Autorenname: Rainer Vollmer
- Der Autorenname sollte klein sein (viel kleiner als der Untertitel)

```html
<!DOCTYPE html>
<html lang="de">
<head>
<meta charset="utf-8">
<title>Kinderwagen-Kraftkurs – Buchcover</title>
<link rel="stylesheet" href="https://fonts.googleapis.com/css2?family=Oswald:wght@600&family=Montserrat:wght@600&family=Patrick+Hand+SC&family=Sacramento&display=swap">
<style>
  :root {
    --slate: #445a60;
    --slate-ink: #3e5359;
    --paper: #ffffff;
    --chalk: #f3f3f1;
    --ink: #1d1d1d;
  }
  html, body {
    margin: 0;
    padding: 0;
    overflow: hidden;
    background: var(--slate);
  }
  .cover {
    position: relative;
    width: 960px;
    height: 1200px;
    background: var(--slate);
    overflow: hidden;
  }
  .cover-art {
    position: absolute;
    inset: 0;
  }
  .title-main {
    font-family: "Oswald", "Arial Narrow", sans-serif;
    font-weight: 600;
  }
  .author {
    font-family: "Montserrat", Arial, sans-serif;
    font-weight: 600;
    letter-spacing: 2.5px;
  }
  .age-note {
    font-family: "Sacramento", cursive;
  }
  .subtitle {
    position: absolute;
    left: 62px;
    top: 931px;
    width: 480px;
    margin: 0;
    font-family: "Patrick Hand SC", "Comic Sans MS", cursive;
    font-size: 26px;
    line-height: 44px;
    letter-spacing: 5.5px;
    text-transform: uppercase;
    text-align: center;
    white-space: nowrap;
    color: var(--chalk);
  }
</style>
</head>
<body>
<main class="cover">
  <svg class="cover-art" width="960" height="1200" viewBox="0 0 960 1200" xmlns="http://www.w3.org/2000/svg">
    <defs>
      <path id="speech-bubble" d="M 118 205 C 86 120, 205 78, 262 110 C 322 76, 432 92, 444 172 C 505 194, 500 292, 472 330 C 482 392, 402 422, 352 405 L 333 468 L 302 412 C 222 432, 110 412, 108 352 C 38 340, 34 232, 118 205 Z"/>
      <clipPath id="bubble-clip"><use href="#speech-bubble"/></clipPath>
      <clipPath id="scene-clip"><ellipse cx="507" cy="664" rx="360" ry="188"/></clipPath>
      <filter id="bubble-shadow" x="-20%" y="-20%" width="140%" height="140%">
        <feDropShadow dx="6" dy="10" stdDeviation="9" flood-color="#000" flood-opacity="0.28"/>
      </filter>
      <filter id="soften" x="-50%" y="-50%" width="200%" height="200%">
        <feGaussianBlur stdDeviation="38"/>
      </filter>
    </defs>

    <!-- speech bubble -->
    <use class="bubble" href="#speech-bubble" fill="var(--paper)" filter="url(#bubble-shadow)"/>

    <!-- title in light over background -->
    <g class="title-block" fill="var(--chalk)">
      <text class="title-main" x="142" y="213" font-size="82" textLength="645" lengthAdjust="spacingAndGlyphs">KINDERWAGEN-KRAFTKURS</text>
      <text class="title-main" x="142" y="277" font-size="54" textLength="645" lengthAdjust="spacingAndGlyphs">FÜR STARKE VÄTER UND FRÖHLICHE KLEINE</text>
    </g>
    <!-- title in dark where it sits on the bubble -->
    <g class="title-block title-on-bubble" fill="var(--slate-ink)" clip-path="url(#bubble-clip)">
      <text class="title-main" x="142" y="213" font-size="82" textLength="645" lengthAdjust="spacingAndGlyphs">KINDERWAGEN-KRAFTKURS</text>
      <text class="title-main" x="142" y="277" font-size="54" textLength="645" lengthAdjust="spacingAndGlyphs">FÜR STARKE VÄTER UND FRÖHLICHE KLEINE</text>
    </g>

    <text class="author" x="179" y="318" font-size="20" fill="var(--ink)">RAINER VOLLMER</text>

    <!-- illustration area: soft tonal field in the scene's main colours -->
    <g class="scene" role="img" aria-label="Illustration: Vater im Vierfüßlerstand macht eine Fitnessübung über seinem auf einer Decke liegenden Baby">
      <ellipse cx="507" cy="664" rx="360" ry="188" fill="var(--paper)"/>
      <g clip-path="url(#scene-clip)" filter="url(#soften)" opacity="0.55">
        <ellipse cx="560" cy="620" rx="120" ry="50" fill="#6b8f8a"/>
        <ellipse cx="700" cy="650" rx="90" ry="60" fill="#e3868a"/>
        <ellipse cx="420" cy="640" rx="140" ry="40" fill="#c9946c"/>
        <ellipse cx="560" cy="770" rx="260" ry="40" fill="#c4c8d2"/>
        <ellipse cx="400" cy="790" rx="80" ry="24" fill="#8fb0d8"/>
      </g>
    </g>

    <!-- hand-drawn arrow pointing at the baby -->
    <g class="pointer-arrow" fill="none" stroke="var(--chalk)" stroke-linecap="round" stroke-linejoin="round">
      <path d="M 884 922 C 850 985, 740 995, 668 962 C 610 935, 560 905, 510 874" stroke-width="7"/>
      <path d="M 508 874 L 556 870 M 508 874 L 530 912" stroke-width="7"/>
    </g>

    <text class="age-note" x="588" y="900" font-size="64" fill="var(--chalk)" textLength="92" lengthAdjust="spacingAndGlyphs">0-3</text>
    <text class="age-note" x="722" y="912" font-size="118" fill="var(--chalk)" textLength="198" lengthAdjust="spacingAndGlyphs">Jahre</text>
  </svg>

  <p class="subtitle">Mit den 33 besten Fitness-<br>Übungen mit Baby Muskeln<br>stärken, Spaß haben und<br>die Vater-Kind-Bindung<br>vertiefen</p>
</main>
</body>
</html>
```